TLR Property - Business Cards

Looking for a business card & general letterhead, signage etc design for our new logo.

Colours:
000a20
0056a2
00b5ef
0088ce
68cef2

Fonts:
Poppins
Karla

Please keep look and feel of new brand - example in the zip package I sent.

```html
<!DOCTYPE html>
<html lang="en">
<head>
<meta charset="utf-8">
<title>TLR Property – Business Cards</title>
<link rel="stylesheet" href="https://fonts.googleapis.com/css2?family=Poppins:wght@400;600;700&display=swap">
<style>
  :root {
    --navy: #000a20;
    --royal: #0056a2;
    --sky: #00b5ef;
    --ocean: #0088ce;
    --ice: #68cef2;
    --ink: #1c1c1c;
    --paper: #ffffff;
    --stage: #9a9a9a;
    --night: #000000;
  }
  * { box-sizing: border-box; margin: 0; padding: 0; }
  html, body { width: 1093px; height: 1200px; overflow: hidden; }
  body {
    background: var(--stage);
    font-family: "Poppins", sans-serif;
    position: relative;
  }
  .card {
    position: absolute;
    left: 264px;
    width: 578px;
    height: 356px;
    border-radius: 28px;
    overflow: hidden;
    box-shadow: 3px 4px 0 rgba(0,0,0,0.85);
  }
  .card--front { top: 226px; background: var(--paper); }
  .card--back { top: 621px; height: 360px; width: 584px; background: var(--night); }

  .brand {
    position: absolute;
    display: flex;
    align-items: center;
    font-weight: 700;
    white-space: nowrap;
  }
  .brand__dot {
    flex: none;
    border-radius: 50%;
    background: var(--ice);
  }
  .brand--front {
    left: 26px;
    top: 148px;
    gap: 12px;
    font-size: 32px;
    color: var(--ocean);
  }
  .brand--front .brand__dot { width: 52px; height: 52px; }
  .brand--back {
    left: 0;
    right: 0;
    top: 142px;
    justify-content: center;
    gap: 18px;
    font-size: 56px;
    line-height: 1;
    color: var(--sky);
  }
  .brand--back .brand__dot { width: 70px; height: 70px; }

  .details {
    position: absolute;
    right: 32px;
    top: 89px;
    text-align: right;
    color: var(--ink);
  }
  .details__name {
    font-weight: 600;
    font-size: 22px;
    line-height: 26px;
    color: var(--royal);
  }
  .details__title {
    font-size: 17px;
    line-height: 20px;
  }
  .rule {
    display: block;
    width: 30px;
    height: 1px;
    background: var(--ocean);
    margin: 14px 0 0 auto;
  }
  .contact { list-style: none; margin-top: 20px; }
  .contact li {
    font-size: 17px;
    line-height: 21px;
    display: flex;
    justify-content: flex-end;
    align-items: center;
    gap: 5px;
  }
  .contact .accent { color: var(--royal); }
  .contact svg { width: 16px; height: 16px; flex: none; }
  .address { margin-top: 20px; font-size: 17px; line-height: 21px; padding-right: 3px; }
</style>
</head>
<body>
  <section class="card card--front">
    <div class="brand brand--front"><span class="brand__dot"></span>TLR Property</div>
    <div class="details">
      <p class="details__name">DANIEL HARTLEY</p>
      <p class="details__title">Managing Director</p>
      <span class="rule"></span>
      <ul class="contact">
        <li>044-555 201 384
          <svg viewBox="0 0 16 16" aria-hidden="true"><path d="M4 1.5l2.2 3-1.3 1.6a8 8 0 0 0 5 5l1.6-1.3 3 2.2-1.6 2.4C7.5 14.5 1.5 8.5 1.6 3.1z" fill="none" stroke="#0056a2" stroke-width="1.8" stroke-linejoin="round"/></svg>
        </li>
        <li>info@tlrproperty.com
          <svg viewBox="0 0 16 16" aria-hidden="true"><rect x="0.5" y="3" width="15" height="10" fill="#0056a2"/><path d="M1 3.5l7 5.5 7-5.5M1 12.5l5-4.5M15 12.5l-5-4.5" stroke="#fff" stroke-width="1.2" fill="none"/></svg>
        </li>
        <li><span>www.<span class="accent">tlrproperty</span>.com</span>
          <svg viewBox="0 0 16 16" aria-hidden="true"><g fill="none" stroke="#0056a2" stroke-width="1.4"><circle cx="8" cy="8" r="6.8"/><ellipse cx="8" cy="8" rx="3" ry="6.8"/><path d="M1.2 8h13.6M2.3 4.5h11.4M2.3 11.5h11.4"/></g></svg>
        </li>
      </ul>
      <span class="rule"></span>
      <p class="address">118, Harbour View Road<br>20871,Eastvale</p>
    </div>
  </section>

  <section class="card card--back">
    <div class="brand brand--back"><span class="brand__dot"></span>TLR Property</div>
  </section>
</body>
</html>
```